Weihnachtskarte für Bikegeschäft
super arbeit. einfach, ohne grossen schnickschnack.
Zielgruppe
wir sind das bikegeschäft in st. moritz und dem oberengadin in der schweiz. wir sind auf high end kunden spezialisiert und bieten verkauf, vermietung und service. wir sind grovantix und tessavoni händler und unsere geschäftsfarben sind gelb schwarz.
Aufgabenstellung
sicher unsere mitarbeiter sollten auf dem flyer sein. statt schwarz gelb kann für die weihnachtskarte auch gold schwarz gebrauchen oder eine eigene idee. ich bin da offen. wenn fotos von st. moritz gefragt sind kann ich diese nachliefern.
Text sollte sein:
FRÖHLICHE WEIHNACHTEN
Vielen Dank für Deine Treue und das Vertrauen, das Du uns entgegenbringst! Wir sind auch über Weihnachten und Neujahr für Dich da – mit spannenden Events wie Radfahren auf Schnee und vielem mehr. Natürlich sind wir wie gewohnt 365 Tage im Jahr für Dich geöffnet. Wir wünschen dir und deinen Liebsten ein schönes Weihnachtsfest und einen guten Rutsch ins neue Jahr.
Dein Team von FENDAmora St. Moritz

```html
<!DOCTYPE html>
<html lang="de">
<head>
<meta charset="utf-8">
<title>FENDAmora – Weihnachtskarte</title>
<link rel="stylesheet" href="https://fonts.googleapis.com/css2?family=Alfa+Slab+One&family=Roboto:wght@400;700&display=swap">
<style>
  :root {
    --yellow: #f2c92e;
    --yellow-light: #f7d84a;
    --black: #1a1a1a;
    --ink: #2b2b2b;
    --white: #ffffff;
    --bg: #ececec;
    --photo-dark: #0e0e0e;
    --photo-mid: #3a2f29;
    --ornament: #d8b43a;
  }
  * { box-sizing: border-box; margin: 0; padding: 0; }
  html, body { width: 1200px; height: 800px; overflow: hidden; }
  body {
    background: var(--bg);
    font-family: "Roboto", sans-serif;
    display: flex;
    align-items: center;
    justify-content: space-between;
    padding: 0 20px;
  }
  .card {
    position: relative;
    width: 570px;
    height: 403px;
    background: linear-gradient(160deg, var(--yellow-light), var(--yellow));
    overflow: hidden;
  }

  /* Front side */
  .photo {
    position: absolute;
    background: radial-gradient(ellipse at 50% 45%, var(--photo-mid) 0%, var(--photo-dark) 70%);
  }
  .photo--top-1 { left: 12px; top: 12px; width: 140px; height: 118px; }
  .photo--top-2 { left: 160px; top: 12px; width: 140px; height: 118px; }
  .photo--bottom-1 { left: 12px; top: 278px; width: 130px; height: 113px; }
  .photo--bottom-2 { left: 150px; top: 278px; width: 130px; height: 113px; }
  .photo--bottom-3 { left: 288px; top: 278px; width: 130px; height: 113px; }
  .photo--bottom-4 { left: 426px; top: 278px; width: 132px; height: 113px; }

  .front__brand {
    position: absolute;
    left: 310px; right: 12px; top: 12px; height: 118px;
    display: flex; align-items: center; justify-content: center;
    font-weight: 700;
    font-size: 34px;
    letter-spacing: 2px;
    color: var(--black);
  }
  .front__band {
    position: absolute;
    left: 0; right: 0; top: 138px; height: 132px;
    background: var(--black);
    display: flex; flex-direction: column; align-items: center; justify-content: center;
  }
  .front__title {
    font-family: "Alfa Slab One", serif;
    color: var(--white);
    font-size: 44px;
    line-height: 1.05;
    letter-spacing: 3px;
    text-align: center;
  }

  /* Back side */
  .ornament {
    position: absolute;
    background: linear-gradient(180deg, transparent, rgba(216,180,58,0.45));
    border-radius: 40px;
  }
  .ornament--left { left: 14px; top: 14px; width: 60px; height: 90px; }
  .ornament--right { right: 14px; top: 14px; width: 70px; height: 90px; }

  .back__content {
    position: absolute;
    left: 70px; right: 70px; top: 24px;
    text-align: center;
    color: var(--ink);
  }
  .back__title {
    font-family: "Alfa Slab One", serif;
    color: var(--black);
    font-size: 36px;
    line-height: 1.05;
    letter-spacing: 2px;
    margin-bottom: 16px;
  }
  .back__text {
    font-size: 11.5px;
    line-height: 1.5;
    margin-bottom: 8px;
  }
  .back__text strong { font-weight: 700; }
  .back__signature { font-size: 11.5px; line-height: 1.45; margin-top: 8px; }

  .back__footer {
    position: absolute;
    left: 24px; right: 24px; bottom: 20px; height: 78px;
    background: var(--black);
    display: flex; align-items: center;
    padding: 0 18px;
    color: var(--white);
  }
  .back__brand {
    width: 170px;
    font-weight: 700;
    font-size: 22px;
    letter-spacing: 1.5px;
  }
  .back__tagline { flex: 1; }
  .back__tagline-head { font-weight: 700; font-size: 12px; margin-bottom: 4px; }
  .back__tagline-text { font-size: 9.5px; line-height: 1.45; }
</style>
</head>
<body>

  <section class="card card--front" aria-label="Vorderseite">
    <div class="photo photo--top-1" role="img" aria-label="Porträt eines Teammitglieds vor schwarzem Hintergrund"></div>
    <div class="photo photo--top-2" role="img" aria-label="Porträt eines Teammitglieds vor schwarzem Hintergrund"></div>
    <div class="front__brand">FENDAmora</div>
    <div class="front__band">
      <h1 class="front__title">FRÖHLICHE<br>WEIHNACHTEN</h1>
    </div>
    <div class="photo photo--bottom-1" role="img" aria-label="Porträt eines Teammitglieds vor schwarzem Hintergrund"></div>
    <div class="photo photo--bottom-2" role="img" aria-label="Porträt eines Teammitglieds vor schwarzem Hintergrund"></div>
    <div class="photo photo--bottom-3" role="img" aria-label="Porträt eines Teammitglieds vor schwarzem Hintergrund"></div>
    <div class="photo photo--bottom-4" role="img" aria-label="Porträt eines Teammitglieds vor schwarzem Hintergrund"></div>
  </section>

  <section class="card card--back" aria-label="Rückseite">
    <div class="ornament ornament--left" role="img" aria-label="Gezeichnete Christbaumkugel und Zuckerstange"></div>
    <div class="ornament ornament--right" role="img" aria-label="Gezeichnete Christbaumkugel und Zuckerstange"></div>
    <div class="back__content">
      <h2 class="back__title">FRÖHLICHE<br>WEIHNACHTEN</h2>
      <p class="back__text">Vielen Dank für Deine Treue und das Vertrauen, das Du uns entgegenbringst! <strong>Wir sind auch über Weihnachten und Neujahr für Dich da – mit spannenden Events wie Radfahren auf Schnee und vielem mehr.</strong> Natürlich sind wir wie gewohnt 365 Tage im Jahr für Dich geöffnet.</p>
      <p class="back__text">Wir wünschen dir und deinen Liebsten ein schönes Weihnachtsfest und einen guten Rutsch ins neue Jahr.</p>
      <p class="back__signature">Dein Team von<br>FENDAmora St. Moritz</p>
    </div>
    <footer class="back__footer">
      <div class="back__brand">FENDAmora</div>
      <div class="back__tagline">
        <p class="back__tagline-head">THE ST. MORITZ BIKE STORE</p>
        <p class="back__tagline-text">your bikestore and service place in st. moritz. grovantix &amp; tessavoni pro store and petit pedal kids bike. Best testbikes in town</p>
      </div>
    </footer>
  </section>

</body>
</html>
```